The Willowbank Growers Garden Nursery Cards

We are looking for a professional nice business card for the Garden Center. I attached our current cards so you have the information. We do have 2 locations so that is also listed. We like the brown fade in the front, but if you have other ideas that is fine.

Also the back of the card we would like to have the ariel picture of the nursery on the card. I have that picture attached.

I also uploaded our logo files for you.

Target Market(s)

Retail

Industry/Entity Type

Retail Garden Center

Contact Information for Business Card

I have uploaded card samples.

Colors

Designer to choose colors to be used in the design.

Requirements
Must have
• Name, email, phone, cell, locations

```html
<!DOCTYPE html>
<html lang="en">
<head>
<meta charset="utf-8">
<title>The Willowbank Growers – Business Cards</title>
<link rel="stylesheet" href="https://fonts.googleapis.com/css2?family=Tinos:wght@700&family=Montserrat:wght@400;600&display=swap">
<style>
  :root {
    --bg: #1d1d1f;
    --brown: #5b3527;
    --brown-dark: #472619;
    --gold: #f3c300;
    --cream: #f6f0b8;
    --white: #ffffff;
    --photo-green: #4f6b34;
    --photo-grey: #8a8780;
    --photo-sky: #9fb1b8;
  }
  * { box-sizing: border-box; margin: 0; padding: 0; }
  html, body { width: 1200px; height: 948px; overflow: hidden; background: var(--bg); }
  .canvas { position: relative; width: 1200px; height: 948px; }

  .card {
    position: absolute; left: 250px; width: 700px; height: 400px;
    border-radius: 22px; overflow: hidden;
    border-bottom: 5px solid var(--gold); border-right: 3px solid var(--gold);
  }
  .card--back { top: 44px; }
  .card--front { top: 504px; background: var(--brown); }

  .aerial-photo {
    position: absolute; inset: 0;
    background:
      radial-gradient(ellipse at 58% 42%, rgba(60,50,40,.55), transparent 55%),
      linear-gradient(160deg, var(--photo-sky) 0%, var(--photo-green) 22%, #6f7a4d 45%, var(--photo-grey) 70%, #a19c92 100%);
  }
  .brand {
    position: absolute; display: flex; align-items: center; gap: 14px;
    font-family: "Tinos", "Times New Roman", serif; font-weight: 700; color: var(--cream);
  }
  .brand__dot { flex: none; border-radius: 50%; background: var(--gold); }
  .card--back .brand { left: 170px; top: 160px; font-size: 34px; }
  .card--back .brand__dot { width: 62px; height: 62px; }

  .card--front .brand { right: 34px; top: 40px; font-size: 24px; width: 260px; line-height: 1.15; }
  .card--front .brand__dot { width: 70px; height: 70px; }

  .person { position: absolute; left: 52px; top: 56px; }
  .person__name {
    font-family: "Tinos", "Times New Roman", serif; font-weight: 700;
    font-size: 42px; color: var(--gold); letter-spacing: 1px; line-height: 1;
  }
  .person__title {
    font-family: "Montserrat", sans-serif; font-size: 17px; color: var(--white);
    letter-spacing: 1px; margin-top: 6px;
  }
  .contact { position: absolute; left: 52px; top: 150px; list-style: none;
    font-family: "Montserrat", sans-serif; font-size: 15px; color: var(--white); line-height: 1.45; }
  .contact li { display: flex; align-items: flex-start; gap: 10px; }
  .contact svg { flex: none; width: 14px; height: 14px; margin-top: 3px; fill: var(--gold); }
  .contact .no-icon { padding-left: 24px; }

  .footer-band {
    position: absolute; left: 0; right: 0; bottom: 12px; height: 44px;
    background: var(--brown-dark);
    border-top: 2px solid var(--gold); border-bottom: 2px solid var(--gold);
    display: flex; align-items: center; justify-content: center; gap: 22px;
    font-family: "Montserrat", sans-serif; font-weight: 600; font-size: 15px; color: var(--white);
    letter-spacing: .5px;
  }
</style>
</head>
<body>
<main class="canvas">
  <section class="card card--back">
    <div class="aerial-photo" role="img" aria-label="Aerial photograph of the nursery grounds with greenhouses, plant rows, trees and parking lot"></div>
    <div class="brand"><span class="brand__dot"></span>The Willowbank Growers</div>
  </section>

  <section class="card card--front">
    <div class="brand"><span class="brand__dot"></span>The Willowbank Growers</div>
    <div class="person">
      <h1 class="person__name">JO MARLOWE</h1>
      <p class="person__title">GARDENS MANAGER</p>
    </div>
    <ul class="contact">
      <li><svg viewBox="0 0 24 24"><path d="M6.6 10.8a15 15 0 0 0 6.6 6.6l2.2-2.2a1 1 0 0 1 1-.25 11.4 11.4 0 0 0 3.6.6 1 1 0 0 1 1 1V20a1 1 0 0 1-1 1A17 17 0 0 1 3 4a1 1 0 0 1 1-1h3.5a1 1 0 0 1 1 1c0 1.25.2 2.45.6 3.6a1 1 0 0 1-.25 1z"/></svg>555-201-0147</li>
      <li><svg viewBox="0 0 24 24"><path d="M7 1h10a2 2 0 0 1 2 2v18a2 2 0 0 1-2 2H7a2 2 0 0 1-2-2V3a2 2 0 0 1 2-2zm0 3v14h10V4zm5 15.5a1 1 0 1 0 0 2 1 1 0 0 0 0-2z"/></svg>555-384-2260</li>
      <li><svg viewBox="0 0 24 24"><path d="M2 5h20v14H2zm2 2v.5l8 5 8-5V7l-8 5z"/></svg>jo@willowbankgrowers.com</li>
      <li><svg viewBox="0 0 24 24"><path d="M12 2a7 7 0 0 1 7 7c0 5-7 13-7 13S5 14 5 9a7 7 0 0 1 7-7zm0 4.5a2.5 2.5 0 1 0 0 5 2.5 2.5 0 0 0 0-5z"/></svg>Fernhill,</li>
      <li class="no-icon">780 Orchard Road Fernhill GA 3172</li>
      <li><svg viewBox="0 0 24 24"><path d="M12 2a7 7 0 0 1 7 7c0 5-7 13-7 13S5 14 5 9a7 7 0 0 1 7-7zm0 4.5a2.5 2.5 0 1 0 0 5 2.5 2.5 0 0 0 0-5z"/></svg>Cedar Bend,</li>
      <li class="no-icon">36 Meadow Lane Cedar Bend GA 3174</li>
    </ul>
    <div class="footer-band">
      <span>orders@willowbankgrowers.com</span><span>|</span><span>www.willowbankgrowers.com</span>
    </div>
  </section>
</main>
</body>
</html>
```